Logo/stationary needed for a Holding Company

Hello I need a logo for my holding company, Millbrook Holdings, LLC. I would like it VERY clean and professional. I am thinking similar to a law firm or financial company. I would appreciate stationary/envelope as well under the address below. Thank you very much.

2738 East 47th Street
Crest Level
Ashford Glen, Illinois 60599

Target Market(s)

Irrelevant for this project

Industry/Entity Type

It Company

Logo Text

Millbrook Holdings, LLC or Millbrook Holdings

Logo styles of interest
Wordmark Logo
Lettermark Logo
Font styles to use
Serif
Sans Serif

Colors
0293ce
0355a3
3277b5
34a7d8
85cae6
85acd3
cee9f5

Requirements
Must have
• company name
Nice to have
• just very clean and professional
Should not have
• n/a

```html
<!DOCTYPE html>
<html lang="en">
<head>
<meta charset="utf-8">
<title>Millbrook Holdings, LLC – Stationery</title>
<link href="https://fonts.googleapis.com/css2?family=Open+Sans:wght@400;600;700&family=Arimo:wght@400&family=Montserrat:wght@600&display=swap" rel="stylesheet">
<style>
  :root {
    --navy: #0355a3;
    --sky: #34a7d8;
    --ink: #0355a3;
    --body: #6a6a6a;
    --paper: #ffffff;
    --backdrop: #e9ecef;
  }
  * { box-sizing: border-box; margin: 0; padding: 0; }
  html, body { width: 1200px; height: 1200px; overflow: hidden; }
  body { background: var(--backdrop); position: relative; font-family: "Open Sans", sans-serif; }

  .letterhead {
    position: absolute; left: 143px; top: 72px; width: 705px; height: 1000px;
    background: var(--paper); box-shadow: 0 2px 10px rgba(0,0,0,.12); overflow: hidden;
  }
  .letterhead__band {
    position: absolute; left: 0; top: 0; width: 705px; height: 70px;
    background: linear-gradient(180deg, var(--navy) 0%, var(--navy) 78%, var(--sky) 78%, var(--sky) 100%);
  }

  .brand { position: absolute; display: flex; align-items: center; gap: 10px; color: var(--navy);
    font-family: "Open Sans", sans-serif; font-weight: 700; white-space: nowrap; }
  .brand__square { border: 3px solid var(--sky); flex: none; }
  .letterhead .brand { right: 32px; top: 108px; font-size: 19px; }
  .letterhead .brand__square { width: 40px; height: 40px; }

  .letter__subject { position: absolute; left: 47px; top: 344px; font-family: "Arimo", sans-serif;
    font-size: 14px; color: #666; }
  .letter__body { position: absolute; left: 49px; top: 396px; width: 490px; font-size: 12px;
    line-height: 24.7px; letter-spacing: .5px; color: var(--body); }
  .letter__body p { margin-bottom: 24.7px; }

  .letter__signature { position: absolute; left: 42px; top: 805px; width: 230px; height: 78px;
    background: linear-gradient(90deg, #f1f1f1, #e4e4e4); }
  .letter__signature-label { position: absolute; left: 54px; top: 895px; font-family: "Arimo", sans-serif;
    font-size: 14.5px; color: #222; }

  .address { position: absolute; text-align: right; font-family: "Arimo", sans-serif; color: var(--ink); }
  .address__pin { position: absolute; }
  .contacts { position: absolute; display: flex; align-items: center; font-family: "Arimo", sans-serif; color: var(--ink); white-space: nowrap; }
  .contacts svg { flex: none; }

  .letterhead .address { right: 80px; top: 900px; font-size: 12.5px; line-height: 13.5px; }
  .letterhead .address__pin { right: 56px; top: 902px; }
  .letterhead .contacts { left: 218px; top: 962px; font-size: 12.3px; }

  .card { position: absolute; left: 694px; width: 406px; height: 232px; background: var(--paper);
    box-shadow: 0 4px 12px rgba(0,0,0,.18); }
  .card--front { top: 376px; }
  .card--back { top: 640px; }
  .card--front .brand { left: 15px; top: 36px; font-size: 13.5px; gap: 6px; }
  .card--front .brand__square { width: 28px; height: 28px; border-width: 2px; }
  .card__name { position: absolute; right: 48px; top: 69px; font-family: "Montserrat", sans-serif;
    font-weight: 600; font-size: 19px; letter-spacing: 1.6px; color: var(--navy); }
  .card__title { position: absolute; right: 64px; top: 95px; font-family: "Open Sans", sans-serif;
    font-size: 7.5px; letter-spacing: 6px; color: var(--navy); }
  .card--front .address { right: 72px; top: 137px; font-size: 10.3px; line-height: 11.8px; }
  .card--front .address__pin { right: 52px; top: 134px; }
  .card--front .contacts { left: 18px; top: 200px; font-size: 9.8px; }

  .card--back .brand { left: 50%; top: 50%; transform: translate(-50%, -50%); font-size: 17px; gap: 10px; }
  .card--back .brand__square { width: 36px; height: 36px; }
</style>
</head>
<body>

<section class="letterhead">
  <div class="letterhead__band" role="img" aria-label="Two-tone blue header band"></div>

  <div class="brand"><span class="brand__square"></span>MILLBROOK HOLDINGS, LLC</div>

  <p class="letter__subject">Subject Line: Loreum ipsum dolor sit amet.</p>

  <div class="letter__body">
    <p>Lorem ipsum dolor sit amet, consectetuer adipiscing elit, sed diam nonummy nibh euismod tincidunt ut laoreet dolore magna aliquam erat volutpat. Ut wisi enim ad minim veniam, quis nostrud exerci tation ullamcorper suscipit lobortis nisl ut aliquip ex ea commodo consequat. Duis autem vel eum iriure dolor in hendrerit in vulputate velit esse molestie consequat, vel illum dolore eu feugiat nulla facilisis.</p>
    <p>Nam liber tempor cum soluta nobis eleifend option congue nihil imperdiet doming id quod mazim placerat facer possim assum. Typi non habent claritatem insitam; est usus legentis in iis qui facit eorum claritatem. Claritas est etiam processus dynamicus.</p>
    <p>Mirum est notare quam littera gothica, quam nunc putamus parum claram, anteposuerit litterarum formas humanitatis per seacula quarta decima.</p>
  </div>

  <div class="letter__signature" role="img" aria-label="Handwritten signature"></div>
  <p class="letter__signature-label">Signature</p>

  <div class="address">2738 East 47th Street<br>Crest Level<br>Ashford Glen, Illinois 60599</div>
  <svg class="address__pin" width="12" height="16" viewBox="0 0 12 16" aria-hidden="true"><path d="M6 0a6 6 0 0 0-6 6c0 4.5 6 10 6 10s6-5.5 6-10a6 6 0 0 0-6-6zm0 8.5a2.5 2.5 0 1 1 0-5 2.5 2.5 0 0 1 0 5z" fill="var(--navy)"/></svg>

  <div class="contacts">
    <span>www.company.com</span>
    <svg style="margin:0 24px 0 16px" width="14" height="14" viewBox="0 0 14 14" aria-hidden="true"><circle cx="7" cy="7" r="6" fill="none" stroke="var(--navy)" stroke-width="1.6"/><path d="M1 7h12M7 1c-3 3-3 9 0 12M7 1c3 3 3 9 0 12" fill="none" stroke="var(--navy)" stroke-width="1.2"/></svg>
    <span>info@company.com</span>
    <svg style="margin:0 26px 0 16px" width="17" height="12" viewBox="0 0 17 12" aria-hidden="true"><rect width="17" height="12" fill="var(--navy)"/><path d="M0 0l8.5 6.5L17 0" fill="none" stroke="#fff" stroke-width="1.2"/></svg>
    <span>+00 1234 56 789</span>
    <svg style="margin-left:18px" width="16" height="16" viewBox="0 0 16 16" aria-hidden="true"><path d="M3.5 0.5l3 3-1.8 2.2c1 2 2.6 3.6 4.6 4.6l2.2-1.8 3 3-2 2.5C7 13.5 2.5 9 0.9 2.5z" fill="var(--navy)"/></svg>
  </div>
</section>

<section class="card card--front">
  <div class="brand"><span class="brand__square"></span>MILLBROOK HOLDINGS, LLC</div>
  <p class="card__name">YOUR NAME</p>
  <p class="card__title">YOUR TITLE</p>
  <div class="address">2738 East 47th Street<br>Crest Level<br>Ashford Glen, Illinois 60599</div>
  <svg class="address__pin" width="10" height="14" viewBox="0 0 12 16" aria-hidden="true"><path d="M6 0a6 6 0 0 0-6 6c0 4.5 6 10 6 10s6-5.5 6-10a6 6 0 0 0-6-6zm0 8.5a2.5 2.5 0 1 1 0-5 2.5 2.5 0 0 1 0 5z" fill="var(--navy)"/></svg>
  <div class="contacts">
    <span>www.company.com</span>
    <svg style="margin:0 11px 0 7px" width="11" height="11" viewBox="0 0 14 14" aria-hidden="true"><circle cx="7" cy="7" r="6" fill="none" stroke="var(--navy)" stroke-width="1.6"/><path d="M1 7h12M7 1c-3 3-3 9 0 12M7 1c3 3 3 9 0 12" fill="none" stroke="var(--navy)" stroke-width="1.2"/></svg>
    <span>info@company.com</span>
    <svg style="margin:0 18px 0 7px" width="14" height="10" viewBox="0 0 17 12" aria-hidden="true"><rect width="17" height="12" fill="var(--navy)"/><path d="M0 0l8.5 6.5L17 0" fill="none" stroke="#fff" stroke-width="1.2"/></svg>
    <span>+00 1234 56 789</span>
    <svg style="margin-left:16px" width="12" height="12" viewBox="0 0 16 16" aria-hidden="true"><path d="M3.5 0.5l3 3-1.8 2.2c1 2 2.6 3.6 4.6 4.6l2.2-1.8 3 3-2 2.5C7 13.5 2.5 9 0.9 2.5z" fill="var(--navy)"/></svg>
  </div>
</section>

<section class="card card--back">
  <div class="brand"><span class="brand__square"></span>MILLBROOK HOLDINGS</div>
</section>

</body>
</html>
```